CD cover design, a Flag for the "Lumen Harbor"

CD cover design needed for the release of a new single called "Lumen Harbor" by www.pelatrask.com. The idea is a flag, the flag of the "Lumen Harbor" the song is about a reinvented Utopia, a perfect social political economical organization, a place where we all want to belong to and feel safe and free, controlled technology, restaured humanity, opportunity, no tolerance for crime. To be celebrated it in every performance.

```html
<!DOCTYPE html>
<html lang="en">
<head>
<meta charset="utf-8">
<title>Lumen Harbor – Single Cover</title>
<link rel="stylesheet" href="https://fonts.googleapis.com/css2?family=Damion&family=Montserrat:wght@500&display=swap">
<style>
  :root {
    --flag-dark: #0b0806;
    --flag-brown: #3a2a1b;
    --flag-rust: #6b4a2a;
    --flag-gold: #8a6a3e;
    --flag-shade: #1c1510;
    --title-white: #ffffff;
    --artist-grey: #c9c9cb;
    --link-green: #3fd13f;
  }
  html, body {
    margin: 0;
    padding: 0;
    width: 1200px;
    height: 1116px;
    overflow: hidden;
    background: var(--flag-dark);
  }
  .cover {
    position: relative;
    width: 1200px;
    height: 1116px;
    overflow: hidden;
  }
  .flag-backdrop {
    position: absolute;
    inset: 0;
    background:
      linear-gradient(162deg, transparent 0%, transparent 14%, rgba(0,0,0,0.92) 22%, rgba(0,0,0,0.85) 30%, transparent 40%),
      linear-gradient(170deg, transparent 45%, rgba(20,16,12,0.55) 55%, transparent 66%),
      linear-gradient(165deg, transparent 70%, rgba(10,8,6,0.7) 82%, transparent 92%),
      radial-gradient(ellipse at 85% 8%, var(--flag-gold) 0%, transparent 35%),
      radial-gradient(ellipse at 15% 95%, var(--flag-rust) 0%, transparent 40%),
      radial-gradient(ellipse at 95% 90%, var(--flag-rust) 0%, transparent 35%),
      linear-gradient(180deg, var(--flag-brown) 0%, var(--flag-shade) 50%, var(--flag-brown) 100%);
  }
  .single-title {
    position: absolute;
    left: 0;
    right: 0;
    top: 360px;
    margin: 0;
    text-align: center;
    font-family: "Damion", cursive;
    font-weight: 400;
    font-size: 168px;
    line-height: 1;
    color: var(--title-white);
    letter-spacing: 2px;
  }
  .artist-name {
    position: absolute;
    left: 0;
    right: 0;
    top: 810px;
    margin: 0;
    text-align: center;
    font-family: "Damion", cursive;
    font-size: 96px;
    line-height: 1;
    color: var(--artist-grey);
  }
  .artist-link {
    position: absolute;
    left: 0;
    right: 0;
    top: 1004px;
    margin: 0;
    padding-left: 30px;
    text-align: center;
    font-family: "Montserrat", sans-serif;
    font-weight: 500;
    font-size: 19px;
    color: var(--link-green);
  }
</style>
</head>
<body>
  <main class="cover">
    <div class="flag-backdrop" role="img" aria-label="Weathered dark brown flag waving, grunge texture with a black fold across the top"></div>
    <h1 class="single-title">Lumen Harbor</h1>
    <p class="artist-name">Pela Trask</p>
    <p class="artist-link">www.pelatrask.com</p>
  </main>
</body>
</html>
```